St Orvel 43rd Festival

We need a poster design for the 43rd St Orvel Youth Festival.
The festival will include a church service, folkloric dancing and a live band. The poster will be primarily in the Cyrillic language so it will need to be editable by us to confirm the writing.
I have attached a older design that we would like to use as a base. The new look of the poster is to be fresh and clean, i have attached an example of the new / clean poster. We would like to incorporate our countries nations colours, red, blue and white like in the example.

You will have to extract the text from the scanned 'old poster' pdf document

I have marked up a image 'my thoughts' to help

Once this poster is finalised we will engage with you further for to design menu poster, entry ticket design etc.

```html
<!DOCTYPE html>
<html lang="sr">
<head>
<meta charset="utf-8">
<title>St Orvel 43rd Youth Festival</title>
<link rel="stylesheet" href="https://fonts.googleapis.com/css2?family=EB+Garamond:wght@400;600;700;800&family=Open+Sans:wght@400;600;700;800&display=swap">
<style>
:root{
  --page:#f1f1f0;
  --navy:#0b1434;
  --navy-deep:#050a20;
  --blue:#2a62a6;
  --blue-light:#4e8bc9;
  --red:#c8102e;
  --red-bright:#e0283c;
  --white:#ffffff;
  --cream:#f4f1ea;
}
*{margin:0;padding:0;box-sizing:border-box}
html,body{width:1200px;height:2310px;overflow:hidden;background:var(--page)}
.poster{
  position:absolute;left:40px;top:362px;width:1120px;height:1586px;overflow:hidden;
  background:radial-gradient(ellipse at 50% 45%,#17224c 0%,var(--navy) 55%,var(--navy-deep) 100%);
  box-shadow:0 18px 40px rgba(0,0,0,.25);
  color:var(--white);
}
.deco{position:absolute;inset:0;width:100%;height:100%}
.intro{position:absolute;top:56px;left:0;width:100%;text-align:center;font-family:"Open Sans",sans-serif;font-size:21px;line-height:23px}
.title-banner{position:absolute;left:185px;top:140px;width:753px;height:89px}
.title-banner svg{position:absolute;inset:0}
.title-banner p{position:relative;text-align:center;font-family:"Open Sans",sans-serif;font-weight:800;font-size:35px;line-height:40px;padding-top:5px}
.emblem{position:absolute;left:62px;top:250px;width:322px;height:287px}
.emblem-name{position:absolute;left:0;top:118px;width:100%;text-align:center;font-family:"EB Garamond",serif;font-weight:700;font-size:46px;color:var(--white)}
.headline{position:absolute;left:408px;top:256px;font-family:"EB Garamond",serif;font-weight:700;font-size:128px;line-height:118px;letter-spacing:1px;color:var(--cream)}
.venue{position:absolute;left:413px;top:504px;font-family:"Open Sans",sans-serif;font-weight:700;font-size:18px}
.friday{position:absolute;left:0;top:560px;width:100%;text-align:center;font-family:"EB Garamond",serif;font-weight:800;font-size:84px;color:var(--red-bright);line-height:90px}
.friday-note{position:absolute;left:0;top:650px;width:100%;text-align:center;font-family:"EB Garamond",serif;font-size:37px}
.day{position:absolute;top:722px;width:493px;height:52px}
.day svg{position:absolute;inset:0}
.day h2{position:relative;text-align:center;font-family:"EB Garamond",serif;font-weight:700;font-size:33px;line-height:52px}
.day-sat{left:48px}.day-sun{left:571px}
.schedule{position:absolute;top:800px;list-style:none;font-family:"EB Garamond",serif;font-weight:700;font-size:21px;line-height:25.5px}
.schedule li{padding-left:24px;position:relative}
.schedule li::before{content:"";position:absolute;left:2px;top:8px;width:10px;height:10px;border-radius:50%;border:3px solid var(--red-bright)}
.schedule-sat{left:100px}.schedule-sun{left:663px}
.photo{position:absolute;top:931px;width:266px;height:266px;border-radius:50%;border:3px solid var(--white)}
.photo-church{left:49px;background:linear-gradient(180deg,#cfe0ee 0%,#c58a5a 50%,#6f7b3c 100%)}
.photo-dance{left:296px;background:linear-gradient(180deg,#6c8a72 0%,#b53a3a 55%,#2b2a2e 100%)}
.photo-food{left:542px;background:radial-gradient(circle at 50% 45%,#d9642c 0%,#7a3a20 55%,#e8e3d8 100%)}
.photo-band{left:794px;background:linear-gradient(180deg,#3a3e46 0%,#e9e7e2 55%,#d9538a 100%)}
.tag{position:absolute;top:1222px;width:195px;height:41px;background:var(--red);text-align:center;font-family:"EB Garamond",serif;font-weight:600;font-size:17px;line-height:41px;text-transform:uppercase}
.tag-church{left:85px}.tag-dance{left:332px}.tag-food{left:578px}.tag-band{left:830px}
.welcome{position:absolute;top:1296px;left:0;width:100%;text-align:center;font-family:"EB Garamond",serif;font-weight:700;font-size:26px}
.blessing{position:absolute;top:1356px;left:0;width:100%;text-align:center;font-family:"EB Garamond",serif;font-weight:600;font-size:15.5px;line-height:19px;text-transform:uppercase}
.contact{position:absolute;top:1437px;left:0;width:100%;text-align:center;font-family:"EB Garamond",serif;font-weight:600;font-size:31px;color:var(--red-bright)}
</style>
</head>
<body>
<main class="poster">
  <svg class="deco" viewBox="0 0 1120 1586" aria-hidden="true">
    <!-- corner flag ribbons -->
    <path d="M0 0 H185 C150 40 110 55 60 55 C35 55 15 70 0 85 Z" fill="var(--white)"/>
    <path d="M0 0 H130 C100 25 70 30 40 30 C20 30 8 38 0 45 Z" fill="var(--blue)"/>
    <path d="M0 0 H80 C60 12 35 14 0 18 Z" fill="var(--red)"/>
    <path d="M1120 0 H880 C920 40 970 60 1030 70 C1070 78 1100 100 1120 125 Z" fill="var(--white)"/>
    <path d="M1120 0 H940 C970 25 1010 38 1060 42 C1090 45 1108 55 1120 65 Z" fill="var(--blue)"/>
    <path d="M1120 0 H1020 C1050 12 1090 16 1120 25 Z" fill="var(--red)"/>
    <!-- bottom-left sash -->
    <path d="M0 1270 L425 1586 H0 Z" fill="var(--white)"/>
    <path d="M0 1290 L400 1586 H0 Z" fill="var(--blue)"/>
    <path d="M0 1270 L425 1586 H160 L0 1455 Z" fill="var(--red)"/>
    <!-- bottom-right twisted ribbon -->
    <path d="M880 1586 C860 1490 900 1390 990 1330 C1040 1300 1090 1300 1120 1320 V1586 Z" fill="var(--white)"/>
    <path d="M930 1586 C915 1500 950 1410 1020 1360 C1060 1335 1100 1340 1120 1360 V1586 Z" fill="var(--blue)"/>
    <path d="M1000 1586 C1000 1520 1020 1440 1070 1395 C1090 1380 1108 1380 1120 1390 V1586 Z" fill="var(--red)"/>
  </svg>

  <p class="intro">Организациони одбор<br>Православне Митрополије Приморске<br>са благословом нашег Преосвећеног Владике Господина Теодора организује и позива на</p>

  <div class="title-banner">
    <svg viewBox="0 0 753 89" preserveAspectRatio="none" aria-hidden="true"><path d="M0 0 H753 L728 44 L753 89 H0 L25 44 Z" fill="var(--red)"/></svg>
    <p>ЧЕТРДЕСЕТ трећи СВЕТООРВЕЛСКИ<br>ОМЛАДИНСКИ ФЕСТИВАЛ</p>
  </div>

  <div class="emblem">
    <svg viewBox="0 0 322 287" width="322" height="287" aria-hidden="true">
      <circle cx="161" cy="143" r="128" fill="var(--blue)" stroke="var(--blue-light)" stroke-width="6"/>
    </svg>
    <p class="emblem-name">St Orvel</p>
  </div>

  <h1 class="headline">YOUTH<br>FESTIVAL</h1>
  <p class="venue">МАНАСТИР НОВИ ОРВЕЛ, 12 LINDEN ROAD - HALL - ACT 2900</p>

  <p class="friday">ПЕТАК - 26 ЈАНУАР</p>
  <p class="friday-note">18.00 ЧАСОВА ВЕЧЕРЊЕ БОГОСЛУЖЕЊЕ</p>

  <div class="day day-sat">
    <svg viewBox="0 0 493 52" preserveAspectRatio="none" aria-hidden="true"><path d="M0 0 H493 L473 52 H0 L22 26 Z" fill="var(--blue)"/></svg>
    <h2>СУБОТА 27. ЈАНУАР 2024</h2>
  </div>
  <div class="day day-sun">
    <svg viewBox="0 0 493 52" preserveAspectRatio="none" aria-hidden="true"><path d="M0 0 H493 L471 26 L493 52 H20 Z" fill="var(--blue)"/></svg>
    <h2>НЕДЕЉА - 28. ЈАНУАР</h2>
  </div>

  <ul class="schedule schedule-sat">
    <li>10.00 Света Архијерејска Литургија</li>
    <li>12.30 Отварање Фестивала</li>
    <li>13.00 Наступи фолклорних група и народно весеље</li>
    <li>18.00 Вечерње Богослужење</li>
  </ul>
  <ul class="schedule schedule-sun">
    <li>10.00 Света Литургија</li>
    <li>11.30 Наставак фолклорних група</li>
    <li>15.00 Недела пехара</li>
    <li>Зав ршетак Фестивала</li>
  </ul>

  <div class="photo photo-church" role="img" aria-label="Photo of the monastery church building"></div>
  <div class="photo photo-dance" role="img" aria-label="Photo of a folkloric dance group in costume"></div>
  <div class="photo photo-food" role="img" aria-label="Photo of grilled meat and salads"></div>
  <div class="photo photo-band" role="img" aria-label="Photo of the live band"></div>

  <p class="tag tag-church">Church Service</p>
  <p class="tag tag-dance">Folkloric Dancing</p>
  <p class="tag tag-food">Food</p>
  <p class="tag tag-band">Live Band</p>

  <p class="welcome">ЧЕКА ВАС ДОМАЋИНСКА КУХИЊА И ПРИЈАТНА СРПСКА МУЗИКА</p>
  <p class="blessing">Добро нам дошли у светоорвелску светињу свих верних срба<br>Аустралије и Новог Зеланда. И на поклоњење недавно пристиглој<br>из манастира Светог Орвела светој икони Богородици Тројеручици!</p>
  <p class="contact">ЗА СВЕ Н ІТЕ СЕ НА ТЕЛ : 0400 555 018</p>
</main>
</body>
</html>
```